Real Estate Fund Needs Flyer showing our current properties

We are a growing real estate fund and we want to show new investors the properties we currently own. There are 4 pictures with descriptions. Also there are quotes and notes regarding the fund throughout the flyer also. The main purpose is to attract new investors to the fund. Pictures are attached. The text in the example needs to be the same on the new design. There are 4 properties. The example only has 3. But Pic titled 517KBramt needs to have this text also:

318 W Marrow Ave., Liberty, MO 64071

The Quillby Residences consist of 20 units. They are located in downtown Liberty, Missouri, adjacent to the Historic Downtown Square. This convenient location is close to City and County offices, shopping, restaurants, and employment centers. Quillby Residences are only blocks from Dorrance Pike College. Liberty is a rapidly growing suburb of Kansas City, Missouri. It is a progressive city with expanding business development and new industry. Located just a few miles north of the Missouri River on Interstate I-35, it is among the largest and fastest growing suburbs in the area. Major employers in Liberty include the Vendrel distribution and operations headquarters for Tosklinfuel.

Target Market(s)

New investors

Industry/Entity Type

Real Estate

Requirements
Must have
• Sleek business like feel.
Nice to have
• Colors matching our brand. Unique backgrounds
• Our website: www.plumtidegroup.example
Should not have
• Our current design is attached. We do not like it at all. The colors aren't right and it's boring.

```html
<!DOCTYPE html>
<html lang="en">
<head>
<meta charset="utf-8">
<title>Recent Acquisitions – Plumtide Group</title>
<link href="https://fonts.googleapis.com/css2?family=Montserrat:wght@400;600;700&family=Open+Sans:wght@400;600&display=swap" rel="stylesheet">
<style>
  :root {
    --navy: #1d3557;
    --slate: #2f4f74;
    --steel: #4d7aa6;
    --sky: #dfe8f1;
    --paper: #ffffff;
    --ink: #2b3440;
    --muted: #5a6676;
  }
  * { box-sizing: border-box; margin: 0; padding: 0; }
  html, body { width: 900px; height: 1200px; overflow: hidden; background: #d9dbde; }
  .flyer {
    position: relative; width: 900px; height: 1200px; background: var(--paper);
    font-family: "Open Sans", Arial, sans-serif; color: var(--ink); overflow: hidden;
  }
  .photo { position: absolute; }
  .hero-photo {
    left: 0; top: 0; width: 900px; height: 240px;
    background: linear-gradient(180deg, #9fc1e0 0%, #c9dcec 45%, #7f8d99 75%, #5c6670 100%);
  }
  .brand {
    position: absolute; right: 40px; top: 24px; width: 250px; height: 120px;
    background: var(--paper); display: flex; flex-direction: column;
    align-items: center; justify-content: center; gap: 6px;
    box-shadow: 0 4px 14px rgba(0,0,0,.18);
  }
  .brand-mark { width: 14px; height: 14px; background: var(--navy); }
  .brand-name {
    font-family: "Montserrat", Arial, sans-serif; font-weight: 600; font-size: 22px;
    letter-spacing: 2px; color: var(--navy); text-transform: uppercase;
  }
  .brand-tag { font-family: "Montserrat", Arial, sans-serif; font-weight: 600; font-size: 13px; color: var(--navy); letter-spacing: 1px; }

  .intro {
    position: absolute; left: 0; top: 180px; width: 900px; height: 240px;
    background: rgba(29,53,87,.93); color: var(--paper);
    padding: 24px 60px 0 50px;
    clip-path: polygon(0 0, 100% 0, 100% 86%, 0 100%);
  }
  .intro h1 {
    font-family: "Montserrat", Arial, sans-serif; font-weight: 600; font-size: 29px;
    line-height: 1.12; text-transform: uppercase; letter-spacing: .5px; margin-bottom: 10px;
  }
  .intro p { font-size: 11.5px; line-height: 1.45; width: 580px; }

  .property { position: absolute; left: 0; width: 900px; height: 170px; }
  .property h2 {
    font-family: "Montserrat", Arial, sans-serif; font-weight: 700; font-size: 17px;
    color: var(--navy); text-transform: uppercase; margin-bottom: 7px; white-space: nowrap;
  }
  .property p { font-size: 11px; line-height: 1.45; color: var(--muted); }
  .details { position: absolute; top: 18px; width: 520px; }
  .photo-right .details { left: 50px; }
  .photo-left .details { left: 360px; width: 510px; }
  .property .photo { top: 0; width: 340px; height: 170px; }
  .photo-right .photo { right: 0; clip-path: polygon(14% 0, 100% 0, 100% 100%, 0 100%); }
  .photo-left .photo { left: 0; clip-path: polygon(0 0, 100% 0, 86% 100%, 0 100%); }
  .tinted { background: var(--sky); }

  .property-kansas { top: 420px; }
  .property-kansas .photo { background: linear-gradient(160deg, #a8c7e4 0%, #b56a4a 45%, #7a3f2c 75%, #6d8a4d 100%); }
  .property-bramt { top: 590px; }
  .property-bramt .photo { background: linear-gradient(170deg, #9fc3e6 0%, #c9a57c 45%, #8c6a4a 80%, #b7b0a3 100%); }
  .property-tessel { top: 760px; }
  .property-tessel .photo { background: linear-gradient(165deg, #b4d0ea 0%, #d9c6a6 45%, #a7865f 80%, #7d8f58 100%); }
  .property-liberty { top: 930px; }
  .property-liberty .details { top: 12px; width: 540px; }
  .property-liberty .photo { width: 320px; background: linear-gradient(165deg, #a9c6e2 0%, #a8704f 45%, #6f4a36 78%, #6f8a52 100%); }

  .footer {
    position: absolute; left: 0; top: 1100px; width: 900px; height: 100px;
    background: var(--navy); color: var(--paper);
    display: flex; align-items: center; padding: 0 40px 0 50px; gap: 30px;
  }
  .footer-note { width: 380px; font-size: 15px; line-height: 1.35; }
  .footer-note .site { font-weight: 600; font-size: 17px; display: block; }
  .footer-addresses { width: 210px; font-size: 10px; line-height: 1.45; opacity: .9; }
  .footer-addresses strong { font-weight: 600; }
  .footer-phones { margin-left: auto; display: flex; flex-direction: column; gap: 8px; }
  .phone { display: flex; align-items: center; gap: 8px; font-family: "Montserrat", Arial, sans-serif; font-weight: 600; font-size: 16px; }
  .phone svg { width: 16px; height: 16px; }
</style>
</head>
<body>
<main class="flyer">
  <div class="photo hero-photo" role="img" aria-label="Photo of a downtown city skyline under a blue sky"></div>

  <div class="brand">
    <span class="brand-mark"></span>
    <span class="brand-name">Plumtide Group</span>
    <span class="brand-tag">Real Estate Fund</span>
  </div>

  <section class="intro">
    <h1>Recent Acquisitions by<br>Plumtide Group</h1>
    <p>Our purchasing phase has commenced! Below are the current properties owned by the fund. Our team has experience in almost all parts of the US and is working hard to acquire additional properties as soon as possible. As an investor, you not only own a piece of everything we currently own but every future acquisition! The quicker you buy in, the quicker you start receiving realized payouts. Our motto: Why own one property when you can own a piece of many?</p>
  </section>

  <section class="property photo-right property-kansas">
    <div class="details">
      <h2>618 Orrin Blvd., Kansas City, MO 64124</h2>
      <p>This property consists of three, eight-unit, walk-up style apartment buildings, totaling twenty-four units. All three buildings are fully occupied and professionally managed. The property sits in a quiet residential area close to schools, shopping and public transit, with easy access to major highways leading to downtown Kansas City and nearby employment centers.</p>
    </div>
    <div class="photo" role="img" aria-label="Photo of a red brick three-storey apartment building with a lawn"></div>
  </section>

  <section class="property photo-left tinted property-bramt">
    <div class="photo" role="img" aria-label="Photo of a tan two-storey four-unit building in Las Vegas"></div>
    <div class="details">
      <h2>517 K Bramt Ave., Las Vegas, NV 89108</h2>
      <p>This beautiful building has four units and is located at its address in Las Vegas. It was fully refurbished in a complete remodel that included new floors, paint and energy efficient fixtures. The property is located close to the Southwest Technology Center and will demand strong rents for years. The nearest schools are within walking distance.</p>
    </div>
  </section>

  <section class="property photo-left property-tessel">
    <div class="photo" role="img" aria-label="Photo of a beige condominium building with balconies"></div>
    <div class="details">
      <h2>2190 Tessel Dr., 201 Las Vegas, NV 89128</h2>
      <p>This luxury condominium is located within a gated community of fourteen buildings with resort style amenities, including a pool, spa, fitness center and covered parking. The unit features two bedrooms, updated appliances and a private balcony. The location offers easy access to shopping, dining and the Summerlin area, making it a strong long-term rental.</p>
    </div>
  </section>

  <section class="property photo-right tinted property-liberty">
    <div class="details">
      <h2>318 W Marrow Ave., Liberty, MO 64071</h2>
      <p>The Quillby Residences consist of 20 units. They are located in downtown Liberty, Missouri, adjacent to the Historic Downtown Square. This convenient location is close to City and County offices, shopping, restaurants, and employment centers. Quillby Residences are only blocks from Dorrance Pike College. Liberty is a rapidly growing suburb of Kansas City, Missouri. It is a progressive city with expanding business development and new industry. Located just a few miles north of the Missouri River on Interstate I-35, it is among the largest and fastest growing suburbs in the area. Major employers in Liberty include the Vendrel distribution and operations headquarters for Tosklinfuel.</p>
    </div>
    <div class="photo" role="img" aria-label="Photo of a brick apartment building near a historic downtown square"></div>
  </section>

  <footer class="footer">
    <p class="footer-note">Additional pictures and properties will be added as they are purchased. Please visit <span class="site">www.plumtidegroup.example</span></p>
    <div class="footer-addresses">
      <p><strong>Mailing:</strong><br>4410 Calloway Blvd Ste 400<br>Beverly Hills, CA 90210</p>
      <p><strong>Leasing:</strong><br>1187 Dunmore St., Los Angeles, CA 90026</p>
    </div>
    <div class="footer-phones">
      <span class="phone"><svg viewBox="0 0 24 24" aria-hidden="true"><path fill="#fff" d="M6.6 10.8a15.1 15.1 0 0 0 6.6 6.6l2.2-2.2c.3-.3.7-.4 1-.2 1.1.4 2.3.6 3.6.6.6 0 1 .4 1 1V20c0 .6-.4 1-1 1A17 17 0 0 1 3 4c0-.6.4-1 1-1h3.5c.6 0 1 .4 1 1 0 1.3.2 2.5.6 3.6.1.3 0 .7-.2 1z"/></svg>(877) 555-0142</span>
      <span class="phone"><svg viewBox="0 0 24 24" aria-hidden="true"><path fill="#fff" d="M6.6 10.8a15.1 15.1 0 0 0 6.6 6.6l2.2-2.2c.3-.3.7-.4 1-.2 1.1.4 2.3.6 3.6.6.6 0 1 .4 1 1V20c0 .6-.4 1-1 1A17 17 0 0 1 3 4c0-.6.4-1 1-1h3.5c.6 0 1 .4 1 1 0 1.3.2 2.5.6 3.6.1.3 0 .7-.2 1z"/></svg>(323) 555-0178</span>
    </div>
  </footer>
</main>
</body>
</html>
```